New PowerPoint Design Project

A well-known speaker needs a visual presence that compliments his amazing, consistent performance onstage. You'll easily improve this deck, and I'll leave it to you whether you stick with the palette defined by the original BLQEMS icons you'll find in the deck, the mishmosh in the deck as it stands, OR get extra points by going with the corporate color palette so our speaking slides fit with Ronan's brands and his three sub-brands. A look at the Ronan subbrand .png in the attached zip file might give you some ideas.
Updates

Just noting that I'm available to answer questions or supply assets you think you'd need. The big design issue I'm looking for someone to solve is how you'll treat the bright clusters of icons in information graphics of the deck.

Target Market(s)

Corporate Executives and wanabees

Requirements
Must have
• The footer needs to have the Dellwyn Bluepath logo and Twitter and Facebook link and you need to do the first 27 slides. The slides past 27 are there simply if you want to use assets from those slides.
Nice to have
• Use the palette document in the zip rather than palette dictated by the BLQEMS icons in the deck (I do not have source for the icons.).

```html
<!DOCTYPE html>
<html lang="en">
<head>
<meta charset="utf-8">
<title>Mission 3. Expand Your Currency</title>
<link href="https://fonts.googleapis.com/css2?family=Graduate&family=Open+Sans:wght@400;700&family=Didact+Gothic&display=swap" rel="stylesheet">
<style>
  :root {
    --page: #ffffff;
    --slide: #fdfcf0;
    --ink: #333335;
    --lime: #8dc63f;
    --lime-dark: #5fa53a;
    --forest: #0f9444;
    --mint: #2bb673;
    --teal: #14a59a;
    --sky: #29abe2;
    --sky-dark: #1b75bc;
    --tan: #c49a6c;
    --tan-dark: #a67c52;
    --slate: #6d6e71;
    --slate-dark: #414042;
    --pyramid-grey: #58595b;
    --pyramid-shade: #3a3a3c;
    --footer: #3a3a3c;
    --footer-box: #2d2d2f;
    --muted: #8a8a8a;
    --badge: #cfcfcf;
    --amber: #f7a21b;
    --body-text: #555557;
  }
  * { margin: 0; padding: 0; box-sizing: border-box; }
  html, body { width: 1200px; height: 900px; overflow: hidden; background: var(--page); }
  body { position: relative; font-family: "Open Sans", Arial, sans-serif; }

  .slide { position: absolute; left: 68px; top: 190px; width: 1080px; height: 607px; background: var(--slide); }
  .slide-number { position: absolute; left: 1098px; top: 200px; width: 37px; height: 37px; border-radius: 50%;
    background: var(--badge); color: #fff; font-weight: 700; font-size: 19px; text-align: center; line-height: 37px; }

  .title { position: absolute; left: 107px; top: 198px; font-family: "Graduate", "Rockwell", serif;
    font-size: 30px; line-height: 36px; color: var(--ink); letter-spacing: -0.5px; white-space: nowrap; }
  .subtitle { position: absolute; left: 107px; top: 237px; font-family: "Graduate", "Rockwell", serif;
    font-size: 30px; line-height: 36px; color: var(--lime); letter-spacing: -0.5px; white-space: nowrap; }
  .title-rule { position: absolute; left: 82px; top: 274px; }

  .pyramid { position: absolute; left: 150px; top: 318px; }
  .pie { position: absolute; left: 730px; top: 300px; }

  .mission-icon { position: absolute; left: 103px; top: 620px; width: 30px; height: 36px;
    background: linear-gradient(90deg, #ef5aa0 0 50%, #6dcff6 50% 100%); }
  .mission { position: absolute; left: 146px; top: 625px; font-family: "Didact Gothic", Arial, sans-serif;
    font-size: 17px; line-height: 24px; color: var(--body-text); letter-spacing: 0.6px; white-space: nowrap; }
  .mission span { display: block; padding-left: 91px; }

  .footer { position: absolute; left: 68px; top: 700px; width: 1080px; height: 90px; background: var(--footer); }
  .footer-strip { position: absolute; left: 68px; top: 790px; width: 1080px; height: 7px; background: var(--amber); }
  .follow { position: absolute; left: 68px; top: 706px; width: 326px; height: 80px; background: var(--footer-box);
    box-shadow: 0 0 14px rgba(0,0,0,.45); padding: 6px 0 0 16px; }
  .follow-label { color: var(--lime); font-weight: 700; font-size: 13px; line-height: 20px; margin-bottom: 6px; }
  .follow-link { color: #fff; font-weight: 700; font-size: 13px; line-height: 21px; display: flex; align-items: center; white-space: nowrap; }
  .follow-link::before { content: ""; width: 14px; height: 14px; background: #d0d0d0; margin: 0 6px 0 2px; flex: none; }
  .tagline { position: absolute; left: 427px; top: 740px; color: #fff; font-weight: 700; font-size: 15px; white-space: nowrap; }
  .tagline em { font-style: normal; color: var(--muted); }
  .brand { position: absolute; left: 862px; top: 706px; width: 280px; height: 80px; background: var(--footer-box);
    box-shadow: 0 0 14px rgba(0,0,0,.45); display: flex; align-items: center; padding-left: 18px; }
  .brand-mark { width: 34px; height: 34px; background: #fff; margin-right: 10px; flex: none; }
  .brand-name { color: #d8d8d8; font-size: 22px; font-weight: 400; white-space: nowrap; }
</style>
</head>
<body>
  <div class="slide"></div>
  <div class="slide-number">6</div>

  <h1 class="title">MISSION 3. EXPAND YOUR CURRENCY</h1>
  <h2 class="subtitle">DO YOUR HOMEWORK</h2>
  <svg class="title-rule" width="540" height="20" viewBox="0 0 540 20">
    <line x1="16" y1="9" x2="532" y2="9" stroke="#333335" stroke-width="2"/>
    <rect x="4" y="2" width="14" height="14" transform="rotate(45 11 9)" fill="none" stroke="#333335" stroke-width="1.5"/>
    <circle cx="11" cy="9" r="3.5" fill="var(--lime)"/>
  </svg>

  <svg class="pyramid" width="470" height="275" viewBox="150 318 470 275">
    <polygon points="320,393 448,393 440,403 328,403" fill="var(--lime-dark)"/>
    <polygon points="385,320 320,393 448,393" fill="var(--lime)"/>
    <text x="385" y="384" text-anchor="middle" fill="#fff" font-family="Open Sans, sans-serif" font-size="13">PERSONAL</text>
    <polygon points="235,480 530,480 520,490 245,490" fill="var(--sky-dark)"/>
    <polygon points="285,403 482,403 530,480 235,480" fill="var(--sky)"/>
    <text x="390" y="464" text-anchor="middle" fill="#fff" font-family="Open Sans, sans-serif" font-size="21">PROFESSIONAL</text>
    <polygon points="152,562 615,562 590,590 177,590" fill="var(--pyramid-shade)"/>
    <polygon points="232,488 535,488 615,562 152,562" fill="var(--pyramid-grey)"/>
    <text x="390" y="553" text-anchor="middle" fill="#fff" font-family="Open Sans, sans-serif" font-size="27">UNIVERSAL</text>
  </svg>

  <svg class="pie" width="360" height="380" viewBox="730 300 360 380" font-family="Open Sans, sans-serif" fill="#fff">
    <g transform="translate(0 22)">
      <path d="M907 478 L1073 478 A166 166 0 0 1 990 621.8 Z" fill="var(--sky-dark)"/>
      <path d="M907 478 L990 621.8 A166 166 0 0 1 824 621.8 Z" fill="var(--tan-dark)"/>
      <path d="M907 478 L824 621.8 A166 166 0 0 1 741 478 Z" fill="var(--slate-dark)"/>
    </g>
    <g stroke="#e6e6e2" stroke-width="4" stroke-linejoin="round">
      <path d="M907 478 L795.9 354.6 A166 166 0 0 1 907 312 Z" fill="var(--forest)"/>
      <path d="M907 478 L907 312 A166 166 0 0 1 1034.2 371.3 Z" fill="var(--mint)"/>
      <path d="M907 478 L1034.2 371.3 A166 166 0 0 1 1073 478 Z" fill="var(--teal)"/>
      <path d="M907 478 L1073 478 A166 166 0 0 1 990 621.8 Z" fill="var(--sky)"/>
      <path d="M907 478 L990 621.8 A166 166 0 0 1 824 621.8 Z" fill="var(--tan)"/>
      <path d="M907 478 L824 621.8 A166 166 0 0 1 741 478 Z" fill="var(--slate)"/>
      <path d="M907 478 L741 478 A166 166 0 0 1 795.9 354.6 Z" fill="var(--lime)"/>
    </g>
    <g font-size="14" text-anchor="middle">
      <text transform="translate(860 355) rotate(-14)"><tspan x="0" y="0">GIVING</tspan><tspan x="0" y="19">BACK</tspan></text>
      <text font-size="11" transform="translate(966 355) rotate(24)">SPIRITUALITY</text>
      <text font-size="11" transform="translate(1034 428) rotate(68)"><tspan x="0" y="0">INTELLECTUAL</tspan><tspan x="0" y="14">SIMULATION</tspan></text>
      <text transform="translate(1019 542) rotate(-60)"><tspan x="0" y="0">PROFESSIONAL</tspan><tspan x="0" y="18">GROWTH</tspan></text>
      <text x="907" y="608">DEEP</text>
      <text x="907" y="630">RELATIONSHIP</text>
      <text transform="translate(804 540) rotate(66)"><tspan x="0" y="0">FINANCIAL</tspan><tspan x="0" y="18">SUCCESS</tspan></text>
      <text transform="translate(786 428) rotate(-60)"><tspan x="0" y="0">PHYSICAL</tspan><tspan x="0" y="18">WELLNESS</tspan></text>
    </g>
  </svg>

  <div class="mission-icon" role="img" aria-label="Small homework notebook icon"></div>
  <p class="mission">MISSION : DO YOUR HOMEWORK ON ONE INDIVIDUAL<span>AND HOW TO HELP.</span></p>

  <div class="footer"></div>
  <div class="footer-strip"></div>
  <div class="follow">
    <p class="follow-label">FOLLOW ME ON :</p>
    <p class="follow-link">https://www.friendwall.com/ronandellwyn</p>
    <p class="follow-link">https://www.chirpline.com/dellwyn</p>
  </div>
  <p class="tagline">Business is Human | <em>Relationships Power Growth.</em></p>
  <div class="brand">
    <span class="brand-mark"></span>
    <span class="brand-name">dellwynbluepath</span>
  </div>
</body>
</html>
```